Business cards for Harborline Consulting (Leadership & Performance Coaching and HR Consulting)

I have a logo (although I'm open to new ideas) and I need this added to a business card. Ultimately, I will also need help with a website. This is an independent consulting firm that is focuses on Leadership, Performance, Executive Coaching and Talent.
Google the story about "one storm, one sailor" ... hence the 1S1S

Target Market(s)

My clients, CEOs, CHROs, COOs

Contact Information for Business Card

Dana K. Wolfe
President
541.553.0871
dwolfe52@ventomail.net
www.HarborlineConsulting.com
3918 Hollowmere Dr., Fairhaven, OR 97321

Font styles to use
Serif
Sans Serif

Colors
ec1f27
0455a3

Requirements
Must have
• Color, be professional
Nice to have
• Something that pops off the card
Should not have
• Be boring.

```html
<!DOCTYPE html>
<html lang="en">
<head>
<meta charset="utf-8">
<title>Harborline Consulting — Business Cards</title>
<link href="https://fonts.googleapis.com/css2?family=Fjalla+One&family=Work+Sans:wght@400;500;600&display=swap" rel="stylesheet">
<style>
  :root {
    --bg: #262626;
    --card: #161616;
    --card-edge: #1f1f1f;
    --accent: #3a9fe0;
    --text: #f2f2f2;
    --muted: #cfcfcf;
  }
  * { box-sizing: border-box; margin: 0; padding: 0; }
  html, body { width: 1200px; height: 900px; overflow: hidden; }
  body {
    background: var(--bg);
    font-family: "Work Sans", Arial, sans-serif;
    color: var(--text);
    display: flex;
    flex-direction: column;
    align-items: center;
    justify-content: center;
    gap: 40px;
  }
  .card {
    position: relative;
    width: 630px;
    height: 360px;
    background: radial-gradient(ellipse at 75% 35%, var(--card-edge), var(--card) 70%);
    box-shadow: 0 12px 30px rgba(0,0,0,.45);
  }
  .card--front {
    display: flex;
    align-items: center;
    justify-content: center;
  }
  .brand__name {
    font-family: "Work Sans", Arial, sans-serif;
    font-weight: 500;
    font-size: 32px;
    letter-spacing: 1px;
    color: var(--muted);
  }
  .identity {
    position: absolute;
    right: 390px;
    top: 132px;
    text-align: right;
  }
  .identity__name {
    font-family: "Fjalla One", "Arial Narrow", sans-serif;
    font-weight: 400;
    font-size: 40px;
    line-height: 1;
    color: var(--accent);
    text-transform: uppercase;
    white-space: nowrap;
  }
  .identity__role {
    font-size: 17px;
    letter-spacing: 1.5px;
    margin-top: 6px;
  }
  .divider {
    position: absolute;
    left: 262px;
    top: 134px;
    width: 2px;
    height: 62px;
    background: var(--accent);
  }
  .contact {
    position: absolute;
    left: 290px;
    top: 136px;
    list-style: none;
    font-size: 16px;
    letter-spacing: 0.8px;
    white-space: nowrap;
  }
  .contact li {
    display: flex;
    align-items: center;
    gap: 12px;
    height: 22px;
  }
  .contact svg { width: 12px; height: 12px; flex: none; }
  .contact .hl { color: var(--accent); }
  .address {
    position: absolute;
    left: 0; right: 0;
    bottom: 44px;
    text-align: center;
    font-size: 17px;
    letter-spacing: 1.5px;
  }
</style>
</head>
<body>
  <section class="card card--front">
    <p class="brand__name">Harborline Consulting</p>
  </section>

  <section class="card card--back">
    <div class="identity">
      <h1 class="identity__name">Dana K. Wolfe</h1>
      <p class="identity__role">President</p>
    </div>
    <span class="divider"></span>
    <ul class="contact">
      <li>
        <svg viewBox="0 0 12 12" aria-hidden="true"><path d="M3 1 L5 3.5 L4 5 Q5 7 7 8 L8.5 7 L11 9 L9.5 11 Q5 10.5 1.5 6 Q0.5 3 3 1Z" fill="var(--accent)"/></svg>
        541.553.0871
      </li>
      <li>
        <svg viewBox="0 0 12 12" aria-hidden="true"><rect x="1" y="2.5" width="10" height="7" fill="none" stroke="var(--accent)" stroke-width="1.2"/><path d="M1 2.5 L6 6.5 L11 2.5" fill="none" stroke="var(--accent)" stroke-width="1.2"/></svg>
        dwolfe@HarborlineConsulting.com
      </li>
      <li>
        <svg viewBox="0 0 12 12" aria-hidden="true"><circle cx="6" cy="6" r="5" fill="none" stroke="var(--accent)" stroke-width="1.1"/><ellipse cx="6" cy="6" rx="2.2" ry="5" fill="none" stroke="var(--accent)" stroke-width="1"/><path d="M1 6 H11" stroke="var(--accent)" stroke-width="1"/></svg>
        <span>www.<span class="hl">HarborlineConsulting</span>.com</span>
      </li>
    </ul>
    <p class="address">3918 Hollowmere Dr. Fairhaven, OR 97321</p>
  </section>
</body>
</html>
```